CBD online business for pets and pet parents needs a new website

We need a website for my new online business. I have left a job of 25 years to do my passion. Helping Pets Live healthy and happy lives. I would like to provide my story so that our customer will know why I have started this business-To help!We will be providing all natural CBD (Hemp) products, specialty items, memorials as well as some products for pet parents. We would like our landing page to have our mission, be informative and easy to navigate and maybe feature our treats and oils for pets. We will need a page for pet products, a page for pet memorials, a page for pet lover products and a page for pet parent products.

Target Market(s)

millennials, boomers, pet lovers

Coding

Coded - Design and coding required

Number of Pages Required

5+ page

Colors
33b8a4

Requirements
Nice to have
• diagram of hemp oil extract benefits for dogs and people

```html
<!DOCTYPE html>
<html lang="en">
<head>
<meta charset="utf-8">
<title>Tailwise Co — Natural Care for Pets and Pet Parents</title>
<link href="https://fonts.googleapis.com/css2?family=Open+Sans:wght@400;600;700;800&display=swap" rel="stylesheet">
<style>
:root{
  --teal:#1a9690;
  --teal-dark:#137a75;
  --ink:#333333;
  --text:#4a4a4a;
  --muted:#f4f4f4;
  --line:#cfcfcf;
  --orange:#f26a1b;
  --price:#e8821e;
  --dark:#1d1d1d;
  --white:#ffffff;
}
*{box-sizing:border-box;margin:0;padding:0}
html,body{width:1200px;height:2989px;overflow:hidden}
body{font-family:"Open Sans",Arial,sans-serif;color:var(--text);background:var(--white);position:relative}
a{color:inherit;text-decoration:none}
.btn{display:inline-block;background:var(--teal);color:var(--white);font-weight:700;text-transform:uppercase;letter-spacing:.5px}

/* top bar */
.topbar{position:absolute;top:0;right:0;width:495px;height:50px;background:#f3f3f3;clip-path:polygon(0 0,100% 0,100% 100%,24px 100%);display:flex;align-items:center;justify-content:flex-end;gap:16px;padding-right:75px;font-size:13px;color:#444}
.topbar .ship{color:var(--teal);font-weight:700;font-size:14px;display:flex;align-items:center;gap:8px;margin-right:10px}
.topbar .sep{color:#666}

/* header */
.logo{position:absolute;left:75px;top:62px;display:flex;align-items:center;gap:10px}
.logo .mark{width:56px;height:56px;border-radius:50%;background:var(--teal)}
.logo .name{font-size:30px;font-weight:700;color:var(--teal)}
.search{position:absolute;left:579px;top:71px;width:367px;height:35px;border:1px solid #bdbdbd;display:flex}
.search span{flex:1;font-size:13px;color:#777;padding:8px 12px}
.search .go{width:46px;background:#333;display:flex;align-items:center;justify-content:center}
.cart{position:absolute;left:996px;top:70px;display:flex;align-items:center;gap:10px;font-size:13px;font-weight:700;color:#333}
.cart .ico{width:36px;height:36px;border-radius:50%;background:var(--teal);display:flex;align-items:center;justify-content:center}
.cart b{color:var(--teal)}
.nav{position:absolute;right:75px;top:130px;display:flex;gap:44px;font-size:13px;font-weight:700;color:#333;text-transform:uppercase}

/* hero */
.hero{position:absolute;top:165px;left:0;width:1200px;height:542px;background:radial-gradient(circle at 18% 15%,#f7c233 0,#d19a2a 22%,#8aa23b 50%,#6f9a3a 75%,#93b24c 100%)}
.hero-card{position:absolute;left:75px;top:187px;width:435px;height:169px;background:rgba(255,252,230,.88);padding:14px 24px}
.hero-card h1{font-size:45px;font-weight:800;color:var(--teal);letter-spacing:2px;line-height:1.1}
.hero-card p{font-size:21px;font-weight:700;color:#222;margin:4px 0 16px}
.hero-card .btn{font-size:15px;padding:9px 19px}
.dots{position:absolute;left:75px;top:497px;display:flex;gap:9px}
.dots i{width:11px;height:11px;border-radius:50%;background:#fff}
.dots i:first-child{background:#111}

/* welcome */
.welcome{position:absolute;top:707px;left:0;width:1200px;height:472px}
.photo{position:absolute}
.welcome .photo{left:75px;top:64px;width:512px;height:340px;background:linear-gradient(135deg,#5a4630,#2d2a2a 55%,#6d5a3e)}
.copy{position:absolute}
.copy h2{font-size:26px;font-weight:700;color:#333;letter-spacing:1px;margin-bottom:16px;white-space:nowrap}
.copy p{font-size:15px;line-height:28.5px;margin-bottom:8px}
.copy .btn{font-size:15px;padding:12px 29px;margin-top:12px}
.welcome .copy{left:614px;top:58px;width:505px}

/* products */
.products{position:absolute;top:1179px;left:0;width:1200px;height:608px;background:var(--muted)}
.tabs{position:absolute;top:57px;left:408px;display:flex;align-items:center;gap:38px}
.tab{font-size:22px;font-weight:700;color:#333;text-transform:uppercase;letter-spacing:.5px}
.tab.active{color:var(--teal);border:1px solid var(--teal);padding:10px 35px}
.grid{position:absolute;top:143px;left:75px;width:1050px;display:flex;justify-content:space-between}
.card{width:239px;text-align:center}
.card .shot{height:263px;border:1px solid var(--line);background:#fff;margin-bottom:20px}
.card .shot div{width:100%;height:100%}
.card h3{font-size:13.5px;font-weight:700;color:#222;text-transform:uppercase}
.card p{font-size:14px;color:#333;margin:3px 0 7px;white-space:nowrap}
.card .price{font-size:15px;font-weight:700;color:var(--price)}
.card .btn{font-size:12px;padding:8px 16px;margin-top:23px}
.arrow{position:absolute;top:362px}

/* info */
.info{position:absolute;top:1787px;left:0;width:1200px;height:470px}
.info .copy{left:77px;top:62px;width:512px}
.info .photo{left:614px;top:69px;width:512px;height:340px;background:radial-gradient(ellipse at 45% 55%,#1c1c1c 0,#2b2b2b 20%,#5a4a35 45%,#a77d4d 75%,#6a5540)}

/* quote */
.quote{position:absolute;top:2257px;left:0;width:1200px;height:293px;background:var(--dark)}
.quote .photo{left:0;top:0;width:497px;height:293px;background:linear-gradient(120deg,#d28a2a,#8a5220 45%,#2b2520 80%)}
.quote blockquote{position:absolute;left:524px;top:80px;width:540px;font-size:23px;line-height:36px;color:#f1f1f1}
.quote cite{position:absolute;left:524px;top:179px;font-style:normal;font-size:19px;font-weight:700;color:var(--teal)}

/* newsletter */
.newsletter{position:absolute;top:2550px;left:0;width:1200px;height:113px;background:linear-gradient(90deg,var(--teal) 0,var(--teal) 62%,#2a8f7c 80%,#4f9a7a 100%)}
.newsletter h2{position:absolute;left:96px;top:40px;font-size:21px;line-height:34px;font-weight:700;color:#fff;letter-spacing:.6px;white-space:nowrap}
.newsletter .field{position:absolute;left:357px;top:38px;width:357px;height:38px;background:#fff;font-size:12px;color:#444;padding:11px 16px}
.newsletter .btn{position:absolute;left:723px;top:38px;height:38px;width:89px;background:var(--orange);font-size:12px;text-align:center;line-height:38px}

/* footer */
.footer{position:absolute;top:2663px;left:0;width:1200px;height:258px}
.col{position:absolute;top:45px}
.col h4{font-size:20px;font-weight:700;color:#333;margin-bottom:8px}
.col li{list-style:none;font-size:13.5px;color:#333;line-height:27.5px}
.social{display:flex;gap:17px;margin-top:16px}
.social span{width:25px;height:25px;border-radius:4px;background:#5a5a5a}
.bottombar{position:absolute;top:2921px;left:0;width:1200px;height:68px;background:#2b2b2b;color:#eee;font-size:12px}
.bottombar p{position:absolute;left:77px;top:27px}
.pay{position:absolute;left:910px;top:20px;display:flex;gap:18px}
.pay span{width:40px;height:26px;background:#fff;border-radius:3px;font-size:9px;font-weight:700;color:#333;display:flex;align-items:center;justify-content:center}
</style>
</head>
<body>

<div class="topbar">
  <a class="ship" href="#"><svg width="16" height="12" viewBox="0 0 16 12"><rect x="0" y="1" width="10" height="8" fill="#333"/><path d="M10 4h3l3 3v2h-6z" fill="#333"/><circle cx="3.5" cy="10" r="1.8" fill="#333"/><circle cx="12.5" cy="10" r="1.8" fill="#333"/></svg>FREE SHIPPING</a>
  <a href="#">Log in</a><span class="sep">I</span><a href="#">Register</a><span class="sep">I</span><a href="#">Favourite</a>
</div>

<a class="logo" href="#"><span class="mark"></span><span class="name">Tailwise Co</span></a>

<div class="search"><span>Search...</span><a class="go" href="#"><svg width="16" height="16" viewBox="0 0 16 16"><circle cx="6.5" cy="6.5" r="5" stroke="#fff" stroke-width="2.2" fill="none"/><path d="M10.5 10.5l4 4" stroke="#fff" stroke-width="2.4"/></svg></a></div>

<a class="cart" href="#"><span class="ico"><svg width="16" height="14" viewBox="0 0 16 14"><path d="M0 1h3l2 8h9l2-6H4.5" stroke="#fff" stroke-width="1.8" fill="none"/><circle cx="6" cy="12" r="1.5" fill="#fff"/><circle cx="13" cy="12" r="1.5" fill="#fff"/></svg></span>MY CART <b>(0)</b></a>

<nav class="nav"><a href="#">Home</a><a href="#">For Dogs</a><a href="#">For Pet Parents</a><a href="#">Blog</a><a href="#">Contact Us</a></nav>

<section class="hero" role="img" aria-label="A woman hugging a fluffy white dog in a sunlit meadow of wildflowers">
  <div class="hero-card">
    <h1>TAILWISE CO</h1>
    <p>Praesent et magna ullamcorper</p>
    <a class="btn" href="#">Shop Now</a>
  </div>
  <div class="dots"><i></i><i></i><i></i><i></i></div>
</section>

<section class="welcome">
  <div class="photo" role="img" aria-label="Founder smiling with her white dog while holding a bottle of hemp oil"></div>
  <div class="copy">
    <h2>WELCOME TO OUR WEBSITE</h2>
    <p>Lorem ipsum dolor sit amet, consectetur adipiscing elit. Sed venenatis tincidunt magna, et suscipit ante sagittis sit amet. Duis neque justo, efficitur eu velit vitae, porttitor suscipit mi. Suspendisse elementum justo in orci volutpat finibus. Pellentesque ullamcorper facilisis lorem, rutrum euismod lorem finibus sit amet.</p>
    <p>Aenean bibendum libero a orci eleifend iaculis. Etiam nec diam non augue accumsan dapibus. Nulla quis accumsan tellus. Aenean volutpat mauris in sollicitudin aliquam.</p>
    <a class="btn" href="#">Read More</a>
  </div>
</section>

<section class="products">
  <div class="tabs"><a class="tab active" href="#">Featured</a><a class="tab" href="#">New Arrivals</a></div>
  <svg class="arrow" style="left:40px" width="22" height="36" viewBox="0 0 22 36"><path d="M18 3L5 18l13 15" stroke="#555" stroke-width="5" fill="none"/></svg>
  <svg class="arrow" style="left:1142px" width="22" height="36" viewBox="0 0 22 36"><path d="M4 3l13 15L4 33" stroke="#555" stroke-width="5" fill="none"/></svg>
  <div class="grid">
    <div class="card"><div class="shot"><div role="img" aria-label="Bone-shaped box and dropper bottle of hemp oil extract" style="background:linear-gradient(135deg,#fff 15%,#1b1b1b 30%,#2a2a2a 70%,#fff 85%)"></div></div><h3>Product Name</h3><p>Morbi id nulla vitae odio accumsan</p><div class="price">$49.59</div><a class="btn" href="#">Add to Cart</a></div>
    <div class="card"><div class="shot"><div role="img" aria-label="Pump bottle of hemp cream with green leaves" style="background:radial-gradient(ellipse at 50% 50%,#c9c2b0 0,#8fa77a 30%,#fff 65%)"></div></div><h3>Product Name</h3><p>Morbi id nulla vitae odio accumsan</p><div class="price">$49.59</div><a class="btn" href="#">Add to Cart</a></div>
    <div class="card"><div class="shot"><div role="img" aria-label="Box and dropper bottle of focus drops" style="background:linear-gradient(90deg,#fff 12%,#141414 14%,#1c1c1c 45%,#fff 50%,#111 58%,#1a1a1a 85%,#fff 88%)"></div></div><h3>Product Name</h3><p>Morbi id nulla vitae odio accumsan</p><div class="price">$49.59</div><a class="btn" href="#">Add to Cart</a></div>
    <div class="card"><div class="shot"><div role="img" aria-label="Black t-shirt with a dog-lover slogan" style="background:#151515"></div></div><h3>Product Name</h3><p>Morbi id nulla vitae odio accumsan</p><div class="price">$49.59</div><a class="btn" href="#">Add to Cart</a></div>
  </div>
</section>

<section class="info">
  <div class="copy">
    <h2>INFORMATION AND STUDIES</h2>
    <p>Lorem ipsum dolor sit amet, consectetur adipiscing elit. Sed venenatis tincidunt magna, et suscipit ante sagittis sit amet. Duis neque justo, efficitur eu velit vitae, porttitor suscipit mi. Suspendisse elementum justo in orci volutpat finibus. Pellentesque ullamcorper facilisis lorem, rutrum euismod lorem finibus sit amet.</p>
    <p>Aenean bibendum libero a orci eleifend iaculis. Etiam nec diam non augue accumsan dapibus. Nulla quis accumsan tellus. Aenean volutpat mauris in sollicitudin aliquam.</p>
    <a class="btn" href="#">Read More</a>
  </div>
  <div class="photo" role="img" aria-label="Dark glass bottle of hemp oil extract standing on a stone surface"></div>
</section>

<section class="quote">
  <div class="photo" role="img" aria-label="Close-up of a shepherd dog resting against its owner"></div>
  <blockquote>"A dog is the only thing on this earth that loves you more than he loves himself."</blockquote>
  <cite>- Hollis Wren</cite>
</section>

<section class="newsletter" role="img" aria-label="Teal band with a faint image of a dog's paw in a hand on the right">
  <h2>NEWSLETTER SIGN UP</h2>
  <div class="field">Email Address</div>
  <a class="btn" href="#">Sign Up</a>
</section>

<footer class="footer">
  <div class="col" style="left:75px"><h4>Navigation</h4><ul><li>Home</li><li>For Dogs</li><li>For Pet Parents</li><li>Blog</li><li>Contact Us</li></ul></div>
  <div class="col" style="left:330px;top:52px"><h4>My Account</h4><ul><li>Morbi id nulla</li><li>Vitae odio accumsan</li><li>Eleifend</li><li>Liberosed leo</li></ul></div>
  <div class="col" style="left:636px"><h4>Quick Links</h4><ul><li>Search</li><li>Contact</li><li>Refund Policy</li><li>Privacy Policy</li><li>Terms of Service</li></ul></div>
  <div class="col" style="left:903px"><h4>Social Media</h4><div class="social"><span aria-label="Social network 1"></span><span aria-label="Social network 2"></span><span aria-label="Social network 3"></span><span aria-label="Social network 4"></span></div></div>
</footer>

<div class="bottombar">
  <p>Copyright © 2019 Company Name. All Right Reserved</p>
  <div class="pay"><span>Payly</span><span>CardCo</span><span>Verit</span><span>Orbix</span></div>
</div>

</body>
</html>
```